New Business Cards for Organic Meat Farm

We need a business card designed for Thornedge Farm, a meat farm in western MA. Our logo uses a hand-drawn woodcut (attached). Our color palette has been simply black and white (shown in notepad and picture of our food truck). While we are based out of western MA, we have ambitions to grow nationally, so our hope is for a classy and memorable card which will be printed on a premium quality stock from a printer like plavix.com.
Target Market(s)
consumers of quality meats, restauranteurs, partnering farms
Industry/Entity Type
Farming and prepared meat products
Contact Information for Business Card
Wendel Ruark, President/Owner, wendel@thornedgefarm.example, mobile: 555-014-2761, phone: 555-019-6083, thornedgefarm.example, facebook: @thornedgefarm, instagram: @thornedgefarmne
Colors
Designer to choose colors to be used in the design.
Look and feel

```html
<!DOCTYPE html>
<html lang="en">
<head>
<meta charset="utf-8">
<title>Thornedge Farm — Business Card</title>
<link rel="stylesheet" href="https://fonts.googleapis.com/css2?family=Jost:wght@400;500;700&display=swap">
<style>
  :root {
    --backdrop: #6a6a6a;
    --card-black: #121212;
    --gloss: #3c3c3c;
    --card-white: #ffffff;
    --ink: #141414;
    --ink-soft: #2a2a2a;
  }
  * { margin: 0; padding: 0; box-sizing: border-box; }
  html, body { width: 900px; height: 1200px; overflow: hidden; }
  body {
    background: var(--backdrop);
    font-family: "Jost", Arial, sans-serif;
    color: var(--ink);
    position: relative;
  }
  .card {
    position: absolute;
    left: 135px;
    width: 631px;
    height: 360px;
  }
  .card-front {
    top: 212px;
    background: var(--card-black);
    display: flex;
    align-items: center;
    justify-content: center;
  }
  .front-wordmark {
    color: var(--gloss);
    font-weight: 500;
    font-size: 46px;
    letter-spacing: 1px;
    margin-top: 40px;
  }
  .card-back {
    top: 628px;
    background: var(--card-white);
  }
  .back-wordmark {
    position: absolute;
    left: 122px;
    top: 104px;
    width: 172px;
    height: 152px;
    display: flex;
    align-items: center;
    justify-content: center;
    text-align: center;
    font-weight: 500;
    font-size: 30px;
    line-height: 1.15;
    color: var(--ink);
  }
  .divider {
    position: absolute;
    left: 315px;
    top: 112px;
    width: 2px;
    height: 135px;
    background: var(--ink);
  }
  .contact {
    position: absolute;
    left: 342px;
    top: 104px;
  }
  .contact-name {
    font-weight: 700;
    font-size: 28px;
    letter-spacing: 0.5px;
    line-height: 1.1;
    text-transform: uppercase;
  }
  .contact-title {
    font-size: 16px;
    color: var(--ink-soft);
    margin-top: 2px;
    margin-bottom: 8px;
  }
  .contact-line {
    display: flex;
    align-items: center;
    gap: 8px;
    font-size: 16px;
    letter-spacing: 0.4px;
    height: 22.5px;
  }
  .contact-line svg { width: 13px; height: 13px; flex: none; fill: var(--ink); }
  .socials {
    position: absolute;
    top: 294px;
    left: 157px;
    display: flex;
    gap: 34px;
    font-size: 16px;
    letter-spacing: 0.3px;
  }
  .social { display: flex; align-items: center; gap: 4px; }
  .social-dot { width: 15px; height: 15px; border-radius: 50%; background: var(--ink); }
</style>
</head>
<body>
  <section class="card card-front">
    <div class="front-wordmark">Thornedge Farm</div>
  </section>

  <section class="card card-back">
    <div class="back-wordmark">Thornedge<br>Farm</div>
    <div class="divider"></div>
    <div class="contact">
      <div class="contact-name">Wendel Ruark</div>
      <div class="contact-title">President/Owner</div>
      <div class="contact-line">
        <svg viewBox="0 0 16 16" aria-hidden="true"><path d="M3.6 1.2l2.3 2.6-1.3 2a9 9 0 005.6 5.6l2-1.3 2.6 2.3-1.4 2.2C7.6 15 1 8.4 1.4 2.6z"/></svg>
        <span>555-019-6083</span>
      </div>
      <div class="contact-line">
        <svg viewBox="0 0 16 16" aria-hidden="true"><path d="M4 0h8a1 1 0 011 1v14a1 1 0 01-1 1H4a1 1 0 01-1-1V1a1 1 0 011-1zm1 2v10h6V2zm3 11a1 1 0 100 2 1 1 0 000-2z"/></svg>
        <span>555-014-2761</span>
      </div>
      <div class="contact-line">
        <svg viewBox="0 0 16 16" aria-hidden="true"><path d="M1 3h14v1.2L8 9 1 4.2zm0 2.6l7 4.8 7-4.8V13H1z"/></svg>
        <span>wendel@thornedgefarm.example</span>
      </div>
      <div class="contact-line">
        <svg viewBox="0 0 16 16" aria-hidden="true"><path d="M8 0a8 8 0 110 16A8 8 0 018 0zm0 1.5c-1 1.2-1.7 3-1.9 5.7h3.8C9.7 4.5 9 2.7 8 1.5zM1.6 7.2h3C4.7 5 5.2 3.2 6 2a6.5 6.5 0 00-4.4 5.2zm8.4-5.2c.8 1.2 1.3 3 1.4 5.2h3A6.5 6.5 0 0010 2zM1.6 8.8A6.5 6.5 0 006 14c-.8-1.2-1.3-3-1.4-5.2zm4.5 0c.2 2.7.9 4.5 1.9 5.7 1-1.2 1.7-3 1.9-5.7zm5.3 0c-.1 2.2-.6 4-1.4 5.2a6.5 6.5 0 004.4-5.2z"/></svg>
        <span>thornedgefarm.example</span>
      </div>
    </div>
    <div class="socials">
      <div class="social"><span class="social-dot"></span><span>@thornedgefarm</span></div>
      <div class="social"><span class="social-dot"></span><span>@thornedgefarmne</span></div>
    </div>
  </section>
</body>
</html>
```